Business Card Design Project

i have the logo designed.
I require designs for the managing director and the general manager.
we need space for email, and a mobile number.
any other cool stuff/design you guys just let me see what you got.
The managing director card could be black, minimalist, and the cards for the rest of the company could be using the green logo.
it has to impress. transportation market is fragmented, we want to appear professional and sophisticated.
Md: Tariq walid hussain
General manager: nabil hussain
Target Market(s)
clients: procurement heads of contracting companies
Industry/Entity Type
Business

```html
<!DOCTYPE html>
<html lang="en">
<head>
<meta charset="UTF-8">
<title>Drovantix – General Manager Business Card</title>
<link rel="stylesheet" href="https://fonts.googleapis.com/css2?family=Oswald:wght@400;500;700&display=swap">
<style>
  :root {
    --backdrop: #d9d9d9;
    --card-white: #ffffff;
    --green-deep: #0b7a3b;
    --green-mid: #2e9a3c;
    --green-light: #8cc63f;
    --card-shadow: rgba(0, 0, 0, 0.18);
  }
  html, body {
    margin: 0;
    padding: 0;
    width: 1200px;
    height: 1000px;
    overflow: hidden;
    background: var(--backdrop);
    font-family: "Oswald", "Arial Narrow", sans-serif;
  }
  .canvas {
    position: relative;
    width: 1200px;
    height: 1000px;
  }
  .card {
    position: absolute;
    left: 220px;
    width: 760px;
    height: 434px;
    background: var(--card-white);
    box-shadow: 0 6px 18px var(--card-shadow);
    overflow: hidden;
  }
  .card--front { top: 36px; }
  .card--back { top: 530px; }

  /* Front: brand name */
  .brand {
    position: absolute;
    right: 70px;
    top: 170px;
    display: flex;
    align-items: center;
    gap: 18px;
  }
  .brand__dot {
    width: 30px;
    height: 30px;
    border-radius: 50%;
    background: var(--green-deep);
  }
  .brand__name {
    font-weight: 700;
    font-size: 78px;
    line-height: 1;
    color: var(--green-deep);
    letter-spacing: 1px;
  }

  /* Back: contact details */
  .contact {
    position: absolute;
    left: 56px;
    top: 250px;
    margin: 0;
    padding: 0;
    list-style: none;
    color: var(--green-deep);
    font-weight: 500;
    font-size: 17px;
    line-height: 24px;
    text-transform: uppercase;
  }
  .contact__item--web { margin-top: 22px; }

  .divider {
    position: absolute;
    left: 0;
    top: 0;
  }

  .holder {
    position: absolute;
    right: 120px;
    top: 246px;
    text-align: right;
  }
  .holder__name {
    margin: 0;
    font-weight: 700;
    font-size: 38px;
    line-height: 1;
    color: var(--green-deep);
    text-transform: uppercase;
  }
  .holder__title {
    position: relative;
    display: inline-block;
    margin-top: 4px;
    padding: 2px 22px 2px 14px;
    font-weight: 500;
    font-size: 20px;
    line-height: 24px;
    color: var(--card-white);
    text-transform: uppercase;
    background: linear-gradient(90deg, var(--green-mid), var(--green-light));
    clip-path: polygon(0 0, 100% 0, calc(100% - 12px) 100%, 0 100%);
  }
</style>
</head>
<body>
<main class="canvas">
  <section class="card card--front" aria-label="Card front">
    <div class="brand">
      <span class="brand__dot"></span>
      <span class="brand__name">Drovantix</span>
    </div>
  </section>

  <section class="card card--back" aria-label="Card back">
    <svg class="divider" width="760" height="434" viewBox="0 0 760 434" aria-hidden="true">
      <defs>
        <linearGradient id="divider-gradient" x1="0" y1="0" x2="1" y2="0">
          <stop offset="0" stop-color="#0b7a3b"/>
          <stop offset="1" stop-color="#8cc63f"/>
        </linearGradient>
      </defs>
      <rect x="40" y="316" width="600" height="4" fill="url(#divider-gradient)"/>
    </svg>

    <ul class="contact">
      <li class="contact__item">generalmanager@drovantix.com</li>
      <li class="contact__item">+65 4810 2297</li>
      <li class="contact__item contact__item--web">www.drovantix.com</li>
    </ul>

    <div class="holder">
      <h1 class="holder__name">Nabil Hussain</h1>
      <div class="holder__title">General Manager</div>
    </div>
  </section>
</main>
</body>
</html>
```